Verpackungsdesign für Handabdruckset
Zielgruppe
Wir sind ein Startup aus dem Schwarzwald und bieten unter unserer Marke KiroLumi Slogan: “Geschenke mit Herz und Seele aus der Heimat” u.a ein Handabdruckset für Paare an.
Unserer Zielgruppe sind Paare, allen Altersgruppen, frisch verliebt oder schon ewig zusammen, die gemeinsame Momente und Erinnerungen schaffen/festhalten möchten. Unser Produkt ist ein Handabdruckset für Paare. Mit unserem Set können Paare Ihre Hände in einer gewünschten Position abformen, sodass sie detailgetreu ihre Hände in Gips verewigt haben.
Aufgabenstellung
1. der Schwarzwald muss thematisiert werden
2. Die Produktbeschriftung muss folgende sein:
“DAS HANDABDRUCKSET
aus dem Schwarzwald”
3. Die Tannen auf dem beigefügten Stockfoto sollen abgebildet sein
4. Unser angehängtes Logo soll mit drauf sein
5. Die Farben des Logos sollen 1:1 im weiteren oder zusätzlichen Designelementen nochmals aufgegriffen werden. Den Styleguide füge ich bei.
6. Die Schriftart soll klar und schnell lesbar sein (uns gefällt Alegreya Sans z.B gut)
7. es soll emotional noch aufgeladen werden und einen kurzen Text wie “Lieblingsmensch” ggf mit einem integrierten Herz enthalten.
9. Es sollen 2 Hände abgebildet sein siehe Stockfoto.
10. das Außenmaß der Kartonage ist 19x19x19cm. Das Design soll aber nur 15x15cm groß sein.
11. Das Design muss die Herstellerkennzeichnung enthalten:
Wendalux Produkte GmbH,
Ahornstieg 17,
79871 Eisenbach
info@kirolumi-beispiel.de
Der Hintergrund sollte nicht weiß sein, da die Kartonage bereits weiß ist. Ein schöner Ton wäre vielleicht Hex: #f4e7c1

```html
<!DOCTYPE html>
<html lang="de">
<head>
<meta charset="utf-8">
<title>KiroLumi – Das Handabdruckset, Faltschachtel</title>
<link href="https://fonts.googleapis.com/css2?family=Alegreya+Sans:ital,wght@0,400;0,500;1,400&family=Alegreya:ital@1&family=Caveat:wght@500&display=swap" rel="stylesheet">
<style>
  :root{
    --page:#ffffff;
    --carton:#f5e9cf;
    --fold:#cfc6b8;
    --brand:#8c7b6b;
    --accent:#d4194e;
    --rose:#e4a9bb;
    --forest:#c45778;
    --forest-deep:#b8496d;
    --forest-light:#ecc7d0;
  }
  *{box-sizing:border-box;margin:0;padding:0}
  html,body{width:1200px;height:1129px;overflow:hidden;background:var(--page)}
  body{position:relative;font-family:"Alegreya Sans",sans-serif;color:var(--accent)}
  .face{position:absolute;width:378px;height:376px;background:var(--carton)}
  .face--outlined{border:1px solid var(--fold)}
  .face--top{left:403px;top:0;height:374px;border:1px solid var(--fold);border-top:none}
  .face--left{left:27px;top:374px}
  .face--front{left:403px;top:374px}
  .face--right{left:781px;top:374px}
  .face--bottom{left:403px;top:750px;height:379px}

  .brand{position:absolute;left:0;right:0;display:flex;flex-direction:column;align-items:center;color:var(--brand)}
  .brand__dot{border-radius:50%;background:var(--rose);opacity:.85}
  .brand__name{font-weight:400;letter-spacing:.02em;line-height:1}

  .brand--large{top:138px}
  .brand--large .brand__dot{width:62px;height:62px;margin-bottom:26px}
  .brand--large .brand__name{font-size:36px}

  .brand--medium{top:36px}
  .brand--medium .brand__dot{width:32px;height:32px;margin-bottom:6px}
  .brand--medium .brand__name{font-size:17px}

  .brand--small{top:45px}
  .brand--small .brand__dot{width:18px;height:18px;margin-bottom:4px}
  .brand--small .brand__name{font-size:12px}

  .product-title{position:absolute;top:116px;left:0;right:0;text-align:center}
  .product-title__lead{font-size:20px;color:var(--rose);display:block;line-height:1.1}
  .product-title__main{font-size:23px;letter-spacing:.05em;display:block;line-height:1.1}
  .product-title__origin{font-family:"Alegreya",serif;font-style:italic;font-size:10px;color:var(--forest);display:block;margin-top:2px}

  .forest{position:absolute;display:block}
  .forest--front{left:39px;top:206px}
  .forest--side{left:39px;top:243px}
  .forest--bottom{left:39px;top:39px}

  .hands{position:absolute;left:124px;top:192px;width:128px;height:80px;border-radius:40px 40px 30px 30px;background:radial-gradient(ellipse at center,#efe0c6 0%,#f5e9cf 75%)}
  .hands__heart{position:absolute;left:184px;top:184px}

  .tagline{position:absolute;left:232px;top:300px;font-family:"Caveat",cursive;font-size:15px;color:var(--carton);transform:rotate(-14deg);transform-origin:left bottom}

  .steps{position:absolute;top:97px;left:60px;right:60px;list-style:none;text-align:center}
  .steps__item{margin-bottom:7px}
  .steps__num{display:inline-flex;width:14px;height:14px;border:1px solid var(--accent);border-radius:50%;align-items:center;justify-content:center;font-size:9px;line-height:1;margin-bottom:6px}
  .steps__text{font-size:9.5px;line-height:1.3}

  .imprint{position:absolute;top:103px;left:0;right:0;text-align:center;font-style:normal;font-size:12.5px;line-height:1.37}
  .imprint__company{font-weight:500}
  .imprint__phone{margin-top:4px}
</style>
</head>
<body>

<section class="face face--top">
  <div class="brand brand--large">
    <span class="brand__dot"></span>
    <span class="brand__name">KiroLumi</span>
  </div>
</section>

<section class="face face--left face--outlined">
  <div class="brand brand--small">
    <span class="brand__dot"></span>
    <span class="brand__name">KiroLumi</span>
  </div>
  <ol class="steps">
    <li class="steps__item"><span class="steps__num">1</span>
      <p class="steps__text">Lorem ipsum dolor sit amet, consectetuer adipiscing elit, sed diam nonummy nibh euismod tincidunt ut laoreet dolore magna aliquam erat volutpat.</p></li>
    <li class="steps__item"><span class="steps__num">2</span>
      <p class="steps__text">Ut wisi enim ad minim veniam, quis Lorem ipsum dolor sit amet, consectetuer adipiscing elit, sed diam nonummy dolore magna aliquam erat volutpat.</p></li>
    <li class="steps__item"><span class="steps__num">3</span>
      <p class="steps__text">Ut wisi enim ad minim veniam, quis nostrud exerci tation ullamcorper suscipit lobortis nisl ut aliquip ex ea.</p></li>
  </ol>
  <svg class="forest forest--side" width="300" height="96" viewBox="0 0 300 96" role="img" aria-label="Tannenwald-Silhouetten in Rosé- und Beerentönen">
    <defs>
      <linearGradient id="forestSide" x1="0" y1="0" x2="0" y2="1">
        <stop offset="0" stop-color="#ecc7d0"/><stop offset=".55" stop-color="#d98ca4"/><stop offset="1" stop-color="#b8496d"/>
      </linearGradient>
    </defs>
    <path d="M0 0 C20 35 55 75 92 96 L0 96 Z" fill="url(#forestSide)"/>
    <path d="M300 0 C280 35 245 75 208 96 L300 96 Z" fill="url(#forestSide)"/>
  </svg>
</section>

<section class="face face--front">
  <div class="brand brand--medium">
    <span class="brand__dot"></span>
    <span class="brand__name">KiroLumi</span>
  </div>
  <h1 class="product-title">
    <span class="product-title__lead">das</span>
    <span class="product-title__main">HANDABDRUCKSET</span>
    <span class="product-title__origin">aus dem Schwarzwald</span>
  </h1>
  <svg class="forest forest--front" width="298" height="132" viewBox="0 0 298 132" role="img" aria-label="Tannenwald-Silhouetten mit Einschnitt in der Mitte">
    <defs>
      <linearGradient id="forestFront" x1="0" y1="0" x2="0" y2="1">
        <stop offset="0" stop-color="#ecc7d0"/><stop offset=".5" stop-color="#dc98ad"/><stop offset="1" stop-color="#b8496d"/>
      </linearGradient>
    </defs>
    <path d="M0 4 L70 14 L135 78 L150 84 L180 74 L298 0 L298 132 L0 132 Z" fill="url(#forestFront)"/>
  </svg>
  <div class="hands" role="img" aria-label="Linienzeichnung zweier Hände, deren kleine Finger sich verhaken"></div>
  <svg class="hands__heart" width="20" height="18" viewBox="0 0 20 18" aria-hidden="true">
    <path d="M10 16 C3 11 1 7 3 4 C5 1 9 2 10 5 C11 2 15 1 17 4 C19 7 17 11 10 16 Z" fill="none" stroke="#d4194e" stroke-width="1.6"/>
  </svg>
  <p class="tagline">Lieblingsmensch</p>
</section>

<section class="face face--right face--outlined">
  <div class="brand brand--small">
    <span class="brand__dot"></span>
    <span class="brand__name">KiroLumi</span>
  </div>
  <address class="imprint">
    <p class="imprint__company">Wendalux Produkte GmbH</p>
    <p>Ahornstieg 17</p>
    <p>79871 Eisenbach</p>
    <p>info@kirolumi-beispiel.de</p>
    <p class="imprint__phone">07652 4180000</p>
  </address>
  <svg class="forest forest--side" width="300" height="96" viewBox="0 0 300 96" role="img" aria-label="Tannenwald-Silhouetten in Rosé- und Beerentönen">
    <defs>
      <linearGradient id="forestRight" x1="0" y1="0" x2="0" y2="1">
        <stop offset="0" stop-color="#ecc7d0"/><stop offset=".6" stop-color="#e0a5b6"/><stop offset="1" stop-color="#c45778"/>
      </linearGradient>
    </defs>
    <path d="M0 14 L40 6 L90 12 L150 4 L210 10 L260 6 L300 12 L300 96 L0 96 Z" fill="url(#forestRight)"/>
  </svg>
</section>

<section class="face face--bottom">
  <svg class="forest forest--bottom" width="298" height="132" viewBox="0 0 298 132" role="img" aria-label="Hängende Tannenwald-Silhouetten in Rosé- und Beerentönen">
    <defs>
      <linearGradient id="forestBottom" x1="0" y1="0" x2="0" y2="1">
        <stop offset="0" stop-color="#b8496d"/><stop offset=".5" stop-color="#dc98ad"/><stop offset="1" stop-color="#ecc7d0"/>
      </linearGradient>
    </defs>
    <path d="M0 0 L298 0 L298 118 L240 128 L180 120 L120 130 L60 122 L0 126 Z" fill="url(#forestBottom)"/>
  </svg>
</section>

</body>
</html>
```